Business Cards Design for the electrical wholesaler: clean bold dynamic :)

We need a business card design that would follow our latest brand guidelines. As an electrical wholesaler we want to bring a fresh look and feel into the industry. The design should be clean bold and dynamic. It should come alive with the renewed energy of our green colour. Our grey colour should keep things balanced and complement the notion of maturity and responsibility. We employ Lato as a corporate font however are not bound by this font and we’re open to interpretation here.

Target Market(s)

Electrical contractors

Industry/Entity Type

Business

Contact Information for Business Card

Logo
Name & Surname: Olena Dovbush
Job Title: Director of Marketing
Email: helen.dovbush@mailvane.example
Cell phone: XXX.XXX.XXXX
Address: 20917 - 87 Ave. Edmonton, AB, Canada. T6K 2R8
Business Phone: 780.555.0187
Website: www.qorvil.example

Font styles to use
Other font styles liked:
• Lato

Requirements
Must have
• Logo & website
Nice to have
• Brand elements - some of them you may find in the attached Brand Guidelines (e.g. three lines on the background signifying "W")

```html
<!DOCTYPE html>
<html lang="en">
<head>
<meta charset="utf-8">
<title>Qorvil Business Card</title>
<link href="https://fonts.googleapis.com/css2?family=Lato:wght@400;700&display=swap" rel="stylesheet">
<style>
  :root {
    --brand-green: #8dc63f;
    --brand-grey: #555759;
    --ink-dark: #4a4a4a;
    --paper: #dedede;
    --white: #ffffff;
  }
  * { margin: 0; padding: 0; box-sizing: border-box; }
  html, body {
    width: 1200px;
    height: 1200px;
    overflow: hidden;
    background: var(--paper);
    font-family: "Lato", sans-serif;
  }
  .stage { position: relative; width: 1200px; height: 1200px; }
  .card {
    position: absolute;
    top: 454px;
    width: 508px;
    height: 290px;
    overflow: hidden;
  }
  .card-front { left: 47px; background: var(--brand-green); }
  .card-back { left: 644px; background: var(--brand-grey); }

  .brand-lockup {
    position: absolute;
    left: 0; right: 0;
    top: 96px;
    display: flex;
    justify-content: center;
    align-items: center;
    gap: 12px;
  }
  .brand-dot {
    width: 30px; height: 30px;
    border-radius: 50%;
    background: var(--white);
  }
  .brand-name {
    color: var(--white);
    font-weight: 700;
    font-size: 50px;
    line-height: 1;
    letter-spacing: 0.01em;
  }
  .front-website {
    position: absolute;
    left: 0; right: 0;
    top: 175px;
    text-align: center;
    color: var(--ink-dark);
    font-weight: 700;
    font-size: 13px;
    letter-spacing: 0.42em;
  }

  .person-name {
    position: absolute;
    left: 46px;
    top: 44px;
    color: var(--brand-green);
    font-weight: 700;
    font-size: 21px;
    letter-spacing: 0.08em;
    text-transform: uppercase;
  }
  .person-title {
    position: absolute;
    left: 46px;
    top: 69px;
    color: var(--brand-green);
    font-size: 11.5px;
    letter-spacing: 0.08em;
  }
  .contact-list {
    position: absolute;
    left: 48px;
    top: 137px;
    list-style: none;
  }
  .contact-item {
    display: flex;
    align-items: center;
    height: 22.5px;
    color: var(--brand-green);
    font-size: 11.5px;
  }
  .contact-icon {
    width: 12px; height: 12px;
    margin-right: 10px;
    flex: none;
  }
</style>
</head>
<body>
<main class="stage">
  <section class="card card-front" aria-label="Card front">
    <div class="brand-lockup">
      <span class="brand-dot"></span>
      <span class="brand-name">qorvil</span>
    </div>
    <p class="front-website">www.qorvil.example</p>
  </section>

  <section class="card card-back" aria-label="Card back">
    <h1 class="person-name">Olena Dovbush</h1>
    <p class="person-title">Director of Marketing</p>
    <ul class="contact-list">
      <li class="contact-item">
        <svg class="contact-icon" viewBox="0 0 12 12"><path d="M6 0.5a4 4 0 0 0-4 4c0 3 4 7 4 7s4-4 4-7a4 4 0 0 0-4-4zm0 5.6a1.6 1.6 0 1 1 0-3.2 1.6 1.6 0 0 1 0 3.2z" fill="#ffffff"/></svg>
        20917 - 87 Ave. Edmonton, AB, Canada. T6K 2R8
      </li>
      <li class="contact-item">
        <svg class="contact-icon" viewBox="0 0 12 12"><path d="M2.4 1l2 2-1 1.3c.6 1.4 1.8 2.6 3.3 3.3L8 6.6l2 2-1.3 1.9C5 10.2 1.8 7 1.5 2.3z" fill="#ffffff"/></svg>
        780.555.0187
      </li>
      <li class="contact-item">
        <svg class="contact-icon" viewBox="0 0 12 12"><rect x="3" y="0.6" width="6" height="10.8" rx="1" fill="none" stroke="#ffffff" stroke-width="1"/><circle cx="6" cy="9.6" r="0.6" fill="#ffffff"/></svg>
        XXX.XXX.XXXX
      </li>
      <li class="contact-item">
        <svg class="contact-icon" viewBox="0 0 12 12"><rect x="0.8" y="2.5" width="10.4" height="7" fill="none" stroke="#ffffff" stroke-width="1"/><path d="M0.8 2.5L6 6.6l5.2-4.1M0.8 9.5l3.8-3.6M11.2 9.5L7.4 5.9" fill="none" stroke="#ffffff" stroke-width="0.9"/></svg>
        helen.dovbush@mailvane.example
      </li>
      <li class="contact-item">
        <svg class="contact-icon" viewBox="0 0 12 12"><g fill="none" stroke="#ffffff" stroke-width="0.9"><circle cx="6" cy="6" r="5"/><ellipse cx="6" cy="6" rx="2.2" ry="5"/><path d="M1 6h10M1.8 3.5h8.4M1.8 8.5h8.4"/></g></svg>
        www.qorvil.example
      </li>
    </ul>
  </section>
</main>
</body>
</html>
```